Hair Salon Brochure

We need a brochure for our hair salon located in Middle Tennessee called Delphine Locks of Harbor Bend. Along with standard services, we offer specialized services and accommodations for individuals on the Autism Spectrum, regardless of background or hair type.
At Delphine Locks of Harbor Bend, our mission is to create a warm and inclusive haven for individuals of all backgrounds, including those on the autism spectrum and their families. We are dedicated to providing not only exceptional hairstyling services but also hands-on education and specialized cutting techniques for clients with natural textured hair. Our goal is to empower our clients with the knowledge and tools necessary to maintain a successful hair care routine, ensuring they leave our salon feeling confident.
We believe in fostering a sense of community, where parents of younger clients are encouraged to learn the proper hair care techniques for their children, promoting healthy practices at home. Our commitment extends beyond just hair; we are here to help you embrace your true self and recognize the beauty that resides within.
At Delphine Locks of Harbor Bend, our passion is to deliver the ultimate client experience, where you can be unapologetically yourself and feel completely at ease. From the moment you step through our doors, you are welcomed not only to discuss your hair concerns but also to engage in meaningful conversations about life. Together, we will collaborate on a personalized plan to achieve your hair goals and transform the way you perceive yourself.
Always remember, when you look good, you feel good, and when you feel good, you can achieve great things. We firmly believe that every individual is 'Radiant In Every Shade,' and we are here to celebrate that beauty with you."
https://www.delphinelocks.net/
Tagline - "Radiant In Every Shade"

```html
<!DOCTYPE html>
<html lang="en">
<head>
<meta charset="utf-8">
<title>Delphine Locks of Harbor Bend – Brochure</title>
<link href="https://fonts.googleapis.com/css2?family=Great+Vibes&family=Montserrat:wght@400;600;700&display=swap" rel="stylesheet">
<style>
:root{
  --blue:#1f63ad;
  --navy:#0f3f7c;
  --orange:#f07b1f;
  --ink:#2a4f86;
  --grey:#5c6470;
  --paper:#ffffff;
  --backdrop:#e8e9eb;
  --photo-a:#3a2a26;
  --photo-b:#7a5a4c;
  --fold:#eef1f5;
}
*{box-sizing:border-box;margin:0;padding:0}
html,body{width:678px;height:1200px;overflow:hidden}
body{background:var(--backdrop);font-family:"Montserrat",sans-serif;color:var(--grey);position:relative}
.spread{position:absolute;left:19px;width:640px;height:480px;background:var(--paper);box-shadow:0 4px 14px rgba(0,0,0,.18);overflow:hidden}
.spread--outside{top:70px}
.spread--inside{top:630px}
.waves{position:absolute;inset:0;width:640px;height:480px;pointer-events:none}
.panel{position:absolute;top:0;width:213px;height:480px;padding:22px 18px}
.panel--1{left:0}.panel--2{left:213px}.panel--3{left:426px}
.script{font-family:"Great Vibes",cursive;color:var(--orange);font-weight:400}
.heading{font-size:30px;line-height:1;margin-bottom:10px}
.body{font-size:7.2px;line-height:1.55;margin-bottom:7px;color:var(--grey)}
.brand{display:flex;align-items:center;justify-content:center;gap:6px;font-weight:700;color:var(--navy);font-size:13px;line-height:1.15;text-align:left}
.brand__dot{width:12px;height:12px;border-radius:50%;background:var(--blue);flex:none}
.label{font-size:9px;font-weight:700;color:var(--orange);margin:12px 0 3px;text-align:center}
.info{font-size:7.5px;line-height:1.5;color:var(--ink);text-align:center}
.photo{position:absolute;background:linear-gradient(160deg,var(--photo-b),var(--photo-a))}
.tagline{position:absolute;left:426px;width:214px;text-align:center}
.tagline__big{font-size:40px;line-height:1}
.tagline__small{font-size:22px;line-height:1.1}
.services{list-style:none;margin-top:6px}
.services li{font-size:8px;line-height:1.35;color:var(--ink);font-weight:600;padding:4px 0;border-bottom:1px solid #dbe4f1}
.lead{font-size:11px;font-weight:700;color:var(--blue);line-height:1.25;margin-bottom:8px}
.subhead{font-size:12px;font-weight:700;color:var(--orange);line-height:1.25;margin-bottom:8px}
.contact{font-size:7.5px;color:var(--ink);font-weight:600;line-height:1.45}
</style>
</head>
<body>

<section class="spread spread--outside">
  <div class="photo" style="left:426px;top:0;width:214px;height:210px" role="img" aria-label="Portrait photo of the salon owner smiling"></div>
  <svg class="waves" viewBox="0 0 640 480" aria-hidden="true">
    <path d="M426 175 C480 205 560 150 640 185 L640 230 C560 200 490 250 426 220 Z" fill="var(--blue)"/>
    <path d="M426 222 C490 252 560 202 640 232 L640 240 C560 210 490 262 426 230 Z" fill="var(--orange)"/>
    <path d="M0 420 C120 380 220 460 340 420 C450 385 540 440 640 410 L640 480 L0 480 Z" fill="var(--blue)"/>
    <path d="M0 412 C120 372 220 452 340 412 C450 377 540 432 640 402 L640 408 C540 438 450 383 340 418 C220 458 120 378 0 418 Z" fill="var(--orange)"/>
    <line x1="213" y1="0" x2="213" y2="480" stroke="var(--fold)"/><line x1="426" y1="0" x2="426" y2="480" stroke="var(--fold)"/>
  </svg>

  <div class="panel panel--1">
    <h2 class="script heading">Our mission</h2>
    <p class="body">At Delphine Locks of Harbor Bend, our mission is to create a warm and inclusive haven for individuals of all backgrounds, including those on the autism spectrum and their families.</p>
    <p class="body">We are dedicated to providing exceptional hairstyling services, hands-on education and specialized cutting techniques for clients with natural textured hair. Our goal is to empower clients with the knowledge and tools to keep a successful hair care routine.</p>
    <p class="body">We believe in fostering community, where parents of younger clients learn proper hair care techniques for their children, promoting healthy practices at home.</p>
    <p class="body">Our commitment extends beyond hair; we are here to help you embrace your true self and the beauty within.</p>
  </div>

  <div class="panel panel--2">
    <div class="brand" style="margin-top:30px"><span class="brand__dot"></span><span>Delphine Locks<br>of Harbor Bend</span></div>
    <h2 class="script heading" style="text-align:center;margin-top:26px">Contact Us</h2>
    <p class="label">Location</p>
    <p class="info">Delphine Locks of Harbor Bend<br>48 Lantern Row Suite 12<br>Harbor Bend, TN 37000</p>
    <p class="label">Opening Hours</p>
    <p class="info">Thursday and Friday: 9:00 am – 1:00 pm</p>
    <p class="label">Website</p>
    <p class="info">https://www.delphinelocks.net/</p>
  </div>

  <div class="tagline" style="top:255px">
    <div class="script tagline__big">Radiant</div>
    <div class="script tagline__small">In Every Shade</div>
    <p class="body" style="padding:8px 20px 0;text-align:center">When you look good, you feel good, and when you feel good, you can achieve great things.</p>
  </div>
</section>

<section class="spread spread--inside">
  <div class="photo" style="left:18px;top:355px;width:177px;height:110px" role="img" aria-label="Photo of the stylist smiling in the salon"></div>
  <svg class="waves" viewBox="0 0 640 480" aria-hidden="true">
    <path d="M0 0 L640 0 L640 40 C540 70 440 20 320 45 C200 70 100 30 0 55 Z" fill="var(--orange)"/>
    <path d="M0 0 L640 0 L640 28 C540 58 440 8 320 33 C200 58 100 18 0 43 Z" fill="var(--blue)"/>
    <rect x="12" y="349" width="189" height="122" fill="none" stroke="var(--blue)" stroke-width="4"/>
    <line x1="213" y1="0" x2="213" y2="480" stroke="var(--fold)"/><line x1="426" y1="0" x2="426" y2="480" stroke="var(--fold)"/>
  </svg>

  <div class="panel panel--1" style="padding-top:68px">
    <h2 class="script heading">Services</h2>
    <ul class="services">
      <li>Specialized Services for Autism Spectrum Individuals</li>
      <li>Hands-on Natural Hair Care Education</li>
      <li>Exceptional Hairstyling Services</li>
      <li>Education for Natural Textured Hair</li>
      <li>Specialized Cutting Techniques</li>
      <li>Empowerment Through Knowledge and Tools</li>
      <li>Dedication to Client Confidence</li>
    </ul>
  </div>

  <div class="panel panel--2" style="padding-top:68px">
    <h2 class="script heading">Special Session</h2>
    <p class="lead">We are not just a salon, we are an experience!</p>
    <p class="body">Our passion is to deliver the ultimate client experience, where you can be unapologetically yourself and feel completely at ease.</p>
    <p class="body">From the moment you step through our doors, you are welcomed to discuss your hair concerns and to share meaningful conversations about life.</p>
    <p class="body">Together we will build a personalized plan to reach your hair goals and transform the way you see yourself.</p>
    <p class="contact" style="margin-top:14px">Marisol Dunne<br>555-014-2290</p>
  </div>

  <div class="panel panel--3" style="padding-top:68px">
    <h3 class="subhead">Proper hair techniques and our goal</h3>
    <p class="body">Parents of younger clients are encouraged to learn the right care methods for their children, so healthy habits continue at home.</p>
    <p class="body">We share simple tools and routines that make each wash, detangle and style calm, gentle and easy to repeat.</p>
    <p class="body">Every person who sits in our chair deserves to feel seen, and we are here to celebrate your beauty with you.</p>
    <p class="contact" style="text-align:right;margin-top:14px">Renee Hollis<br>555-014-2290</p>
    <div class="brand" style="position:absolute;right:18px;bottom:28px;font-size:11px"><span class="brand__dot"></span><span>Delphine Locks<br>of Harbor Bend</span></div>
  </div>
</section>

</body>
</html>
```